Word Cloud Graphic Wallpaper design

The following sentences need to be put together in an ai file of the size : 70" wide and 108" high . This will be used as a wall paper. Inspirational image is attached. (We have also attached a rough idea showing you the wall it would go one- DO NOT REPLICATE THE LAYOUT OF THE SENTENCES-This only shows you how we will be using your file)

Sentences are:

Dentistry is not Expensive Neglect is!
Smiles are free but they are worth alot.
Don't Forget to Floss!
Put on your best SMILE everyday!
Be the reason someone smiles today.
Let your SMILE CHANGE THE WORLD, don't let the world change your smile.
Make your smile your signature accessory!

These should be in different fonts (clean modern fonts only please- no cursive or busy fonts - Helvetica Neue, Arial and fonts such as those are preferred) and sizes and should be easily legible (minimum font height 4"). Repetitions are ok if needed to fill space.

Font styles to use
Sans Serif

Requirements
Must have
• hese should be in different fonts (clean modern fonts only please- no cursive or busy fonts - Helvetica Neue, Arial and fonts such as those) and sizes and should be easily legible (minimum font height 4"). Repetitions are ok if needed to fill space.
Should not have
• Cursive, busy, fonts.

```html
<!DOCTYPE html>
<html lang="en">
<head>
<meta charset="utf-8">
<title>Smile Word Cloud Wallpaper</title>
<link rel="stylesheet" href="https://fonts.googleapis.com/css2?family=Anton&family=Archivo+Black&family=Montserrat:wght@300;700;800&family=Open+Sans:wght@400&family=Oswald:wght@600;700&family=Roboto:wght@700&family=Roboto+Condensed:wght@400;700&display=swap">
<style>
  :root {
    --sky: #00c6f8;
    --haze: #ffffff;
    --sheet: #ffffff;
    --azure: #0a84e6;
    --sky-blue: #0095e8;
    --royal: #0000e0;
    --red: #ff0000;
    --pink: #ffa8f0;
    --yellow: #ffff00;
    --magenta: #ff00ff;
    --purple: #9900cc;
    --olive: #d4c000;
    --orange: #ff6600;
  }
  html, body {
    margin: 0;
    width: 1200px;
    height: 1200px;
    overflow: hidden;
    background: var(--sky);
  }
  .wallpaper { display: block; width: 1200px; height: 1200px; }
  .sheet { fill: var(--sheet); stroke: #9ab; stroke-width: 1; }

  .geometric { font-family: "Montserrat", sans-serif; }
  .black { font-family: "Archivo Black", sans-serif; }
  .poster { font-family: "Anton", sans-serif; }
  .condensed { font-family: "Oswald", sans-serif; font-weight: 700; }
  .narrow { font-family: "Roboto Condensed", sans-serif; font-weight: 700; }
  .humanist { font-family: "Open Sans", sans-serif; }
  .grotesk { font-family: "Roboto", sans-serif; font-weight: 700; }

  .c-azure { fill: var(--azure); }
  .c-sky { fill: var(--sky-blue); }
  .c-royal { fill: var(--royal); }
  .c-red { fill: var(--red); }
  .c-magenta { fill: var(--magenta); }
  .c-purple { fill: var(--purple); }
  .c-orange { fill: var(--orange); }

  .outline-red { stroke: var(--red); stroke-width: 3; paint-order: stroke; }
  .outline-yellow { stroke: var(--yellow); stroke-width: 2; paint-order: stroke; }
  .outline-blue { stroke: var(--sky-blue); stroke-width: 3; paint-order: stroke; }
  .fill-pink { fill: var(--pink); }
  .fill-yellow { fill: var(--yellow); }
  .fill-olive { fill: var(--olive); }
</style>
</head>
<body>
<svg class="wallpaper" viewBox="0 0 1500 1500" xmlns="http://www.w3.org/2000/svg">
  <defs>
    <radialGradient id="haze-right" cx="0.5" cy="0.5" r="0.5">
      <stop offset="0" stop-color="var(--haze)" stop-opacity="1"/>
      <stop offset="1" stop-color="var(--haze)" stop-opacity="0"/>
    </radialGradient>
  </defs>

  <!-- sky backdrop -->
  <rect width="1500" height="1500" fill="var(--sky)"/>
  <ellipse cx="1400" cy="410" rx="420" ry="120" fill="url(#haze-right)"/>
  <ellipse cx="80" cy="900" rx="420" ry="110" fill="url(#haze-right)"/>

  <!-- poster sheet -->
  <rect class="sheet" x="272" y="12" width="956" height="1476"/>

  <!-- Dentistry is not / Expensive Neglect is! -->
  <g class="headline">
    <text class="geometric c-azure" font-weight="700" font-size="108" x="285" y="110" textLength="663" lengthAdjust="spacingAndGlyphs">Dentistry is n</text>
    <circle cx="1010" cy="82" r="52" fill="var(--red)" stroke="var(--azure)" stroke-width="10"/>
    <text class="geometric c-azure" font-weight="700" font-size="108" x="1073" y="110" textLength="44" lengthAdjust="spacingAndGlyphs">t</text>
    <text class="geometric c-azure" font-weight="300" font-size="100" x="285" y="195" textLength="495" lengthAdjust="spacingAndGlyphs">Expensive</text>
    <text class="narrow c-azure" font-size="140" x="780" y="222" textLength="72" lengthAdjust="spacingAndGlyphs">N</text>
    <text class="narrow c-azure" font-size="100" x="852" y="195" textLength="363" lengthAdjust="spacingAndGlyphs">eglect is!</text>
  </g>

  <!-- Smiles are free but they are worth alot. -->
  <g class="smiles-free">
    <text class="black fill-pink outline-red" font-size="148" x="288" y="335" textLength="454" lengthAdjust="spacingAndGlyphs">Smiles</text>
    <text class="humanist c-red" font-size="90" x="745" y="335" textLength="140" lengthAdjust="spacingAndGlyphs">are</text>
    <text class="poster fill-yellow outline-red" font-size="170" x="885" y="370" textLength="330" lengthAdjust="spacingAndGlyphs">free</text>
    <text class="humanist c-red" font-size="108" x="285" y="412" textLength="608" lengthAdjust="spacingAndGlyphs">but they are</text>
    <text class="black c-red" font-size="92" x="905" y="445" textLength="310" lengthAdjust="spacingAndGlyphs">worth</text>
    <text class="black c-red" font-size="92" x="980" y="515" textLength="230" lengthAdjust="spacingAndGlyphs">alot.</text>
  </g>

  <!-- Don't Forget to Floss! -->
  <g class="floss">
    <text class="condensed c-magenta" font-size="112" x="287" y="500" textLength="248" lengthAdjust="spacingAndGlyphs">Don'T</text>
    <text class="condensed c-magenta" font-size="104" x="287" y="587" textLength="235" lengthAdjust="spacingAndGlyphs">Forge</text>
    <text class="condensed c-magenta" font-size="136" x="520" y="632" textLength="66" lengthAdjust="spacingAndGlyphs">T</text>
    <text class="condensed c-magenta" font-size="74" x="395" y="662" textLength="85" lengthAdjust="spacingAndGlyphs" transform="rotate(-18 437 640)">to</text>
    <text class="poster c-magenta" font-size="130" x="287" y="785" textLength="270" lengthAdjust="spacingAndGlyphs">Floss!</text>
  </g>

  <!-- Put on your best SMILE everyday! -->
  <g class="best-smile">
    <text class="grotesk c-royal" font-size="112" x="577" y="520" textLength="338" lengthAdjust="spacingAndGlyphs">Put on</text>
    <text class="grotesk c-royal" font-size="112" x="655" y="595" textLength="250" lengthAdjust="spacingAndGlyphs">your</text>
    <text class="grotesk c-royal" font-size="112" x="907" y="605" textLength="280" lengthAdjust="spacingAndGlyphs">best</text>
    <text class="grotesk fill-olive outline-red" font-size="150" x="725" y="725" textLength="490" lengthAdjust="spacingAndGlyphs">SMILE</text>
    <text class="narrow fill-olive outline-red" font-size="82" x="730" y="800" textLength="370" lengthAdjust="spacingAndGlyphs">EVERYda</text>
    <text class="grotesk fill-olive outline-red" font-size="230" x="1092" y="860" textLength="115" lengthAdjust="spacingAndGlyphs">y</text>
    <text class="grotesk fill-olive outline-red" font-size="90" x="1172" y="905" transform="rotate(15 1190 870)">!</text>
  </g>

  <!-- Be the reason someone smiles today. -->
  <g class="be-the-reason">
    <text class="grotesk c-purple" font-size="98" x="573" y="710" textLength="117" lengthAdjust="spacingAndGlyphs">Be</text>
    <text class="grotesk c-purple" font-size="104" x="573" y="800" textLength="154" lengthAdjust="spacingAndGlyphs">the</text>
    <text class="grotesk c-purple outline-yellow" font-size="98" x="572" y="860" textLength="316" lengthAdjust="spacingAndGlyphs">reason</text>
    <text class="grotesk c-purple outline-yellow" font-size="98" x="570" y="922" textLength="442" lengthAdjust="spacingAndGlyphs">someonE</text>
    <text class="grotesk c-purple outline-yellow" font-size="96" x="597" y="1003" textLength="615" lengthAdjust="spacingAndGlyphs">smiles toDAY.</text>
  </g>

  <!-- Let your SMILE change the world, don't let the world change your smile. -->
  <g class="change-world">
    <text class="grotesk c-sky" font-size="92" x="287" y="855" textLength="143" lengthAdjust="spacingAndGlyphs">Let</text>
    <text class="grotesk c-sky" font-size="92" x="287" y="910" textLength="208" lengthAdjust="spacingAndGlyphs">your</text>
    <text class="geometric c-sky" font-weight="800" font-size="92" x="287" y="1008" textLength="288" lengthAdjust="spacingAndGlyphs">SMILE</text>
    <text class="geometric c-sky" font-weight="800" font-size="95" x="287" y="1085" textLength="833" lengthAdjust="spacingAndGlyphs">change the world,</text>
    <text class="black fill-yellow outline-blue" font-size="92" x="290" y="1170" textLength="830" lengthAdjust="spacingAndGlyphs">don't let the world</text>
    <text class="narrow fill-yellow outline-blue" font-size="118" transform="translate(1128 1100) rotate(90)" x="0" y="0" textLength="375" lengthAdjust="spacingAndGlyphs">CHANGE</text>
    <text class="narrow fill-yellow outline-blue" font-size="100" transform="translate(1042 1185) rotate(90)" x="0" y="0" textLength="195" lengthAdjust="spacingAndGlyphs">your</text>
    <text class="narrow fill-yellow outline-blue" font-size="90" transform="translate(967 1215) rotate(90)" x="0" y="0" textLength="260" lengthAdjust="spacingAndGlyphs">smile.</text>
  </g>

  <!-- Make your smile your signature accessory! -->
  <g class="signature">
    <text class="condensed c-orange" font-size="108" x="287" y="1268" textLength="378" lengthAdjust="spacingAndGlyphs">Makeyour</text>
    <text class="black c-orange outline-red" font-size="92" x="660" y="1280" textLength="300" lengthAdjust="spacingAndGlyphs">sMile</text>
    <text class="condensed c-orange" font-size="86" x="307" y="1350" textLength="158" lengthAdjust="spacingAndGlyphs">your</text>
    <text class="condensed c-orange" font-size="118" x="497" y="1373" textLength="458" lengthAdjust="spacingAndGlyphs">SiGnature</text>
    <text class="black c-orange outline-red" font-size="118" x="287" y="1470" textLength="668" lengthAdjust="spacingAndGlyphs">ACCESSorY!</text>
  </g>
</svg>
</body>
</html>
```